Candle company needs a label for candle

Looking for a designer to create my candle label. I am going to attach a few pictures of my vision for the label as well as my Company Logo and jar I have puchased. I'm going for the modern rustic feel but you are the designer and have full trust in your abilities. The label is going to be printed on Kraft paper (2x3) so looking for the font to be black. The candle label MUST include the following information:
Candle Birchway Co.
NO. 01: Eucalyptus + Spearmint
Handmade In NJ
Soy Wax
9oz

Industry/Entity Type

Candle Industry

Colors

Designer to choose colors to be used in the design.

Requirements
Should not have
• Any images

```html
<!DOCTYPE html>
<html lang="en">
<head>
<meta charset="utf-8">
<title>Candle Birchway Co. – Eucalyptus + Spearmint Label</title>
<link rel="stylesheet" href="https://fonts.googleapis.com/css2?family=Josefin+Sans:wght@300&display=swap">
<style>
  :root {
    --page: #ffffff;
    --ink: #111111;
    --rule: #1a1a1a;
  }
  * { box-sizing: border-box; margin: 0; padding: 0; }
  html, body {
    width: 1200px;
    height: 960px;
    overflow: hidden;
    background: var(--page);
  }
  .canvas {
    position: relative;
    width: 1200px;
    height: 960px;
    background: var(--page);
    font-family: "Josefin Sans", sans-serif;
    font-weight: 300;
    color: var(--ink);
  }
  .label-frame {
    position: absolute;
    left: 78px;
    top: 197px;
    width: 1044px;
    height: 566px;
    border: 6px solid var(--rule);
  }
  .brand-name {
    position: absolute;
    left: 0;
    top: 352px;
    width: 1200px;
    text-align: center;
    font-weight: 300;
    font-size: 48px;
    line-height: 60px;
    letter-spacing: 0.02em;
    white-space: nowrap;
  }
  .product-table {
    position: absolute;
    left: 346px;
    top: 560px;
    width: 508px;
    height: 172px;
    border: 2px solid var(--rule);
    display: grid;
    grid-template-columns: 256px 179px 1fr;
    grid-template-rows: 71px 1fr;
    font-size: 22px;
    letter-spacing: 0.05em;
  }
  .product-table .cell {
    display: flex;
    align-items: center;
    justify-content: center;
    white-space: nowrap;
    padding-top: 4px;
  }
  .scent-name {
    grid-column: 1 / 4;
    border-bottom: 2px solid var(--rule);
  }
  .origin,
  .wax-type {
    border-right: 2px solid var(--rule);
  }
  .net-weight { letter-spacing: 0.02em; }
</style>
</head>
<body>
  <main class="canvas">
    <section class="label-frame" aria-label="Candle label"></section>

    <h1 class="brand-name">Candle Birchway Co.</h1>

    <div class="product-table">
      <div class="cell scent-name">No. 01 EUCALYPTUS + SPEARMINT</div>
      <div class="cell origin">HANDMADE IN NJ</div>
      <div class="cell wax-type">SOY WAX</div>
      <div class="cell net-weight">9oz</div>
    </div>
  </main>
</body>
</html>
```